Kelvar Systems Website

Website design for our company: Kelvar Systems.
The website should look fresh and IT focused. Please have a look at http://www.kelvarsystems.net.au/ for our current design. We want something fresh and new, professional looking, in WordPress so we can easily make changes.

Industry/Entity Type

It Company

```html
<!DOCTYPE html>
<html lang="en">
<head>
<meta charset="utf-8">
<title>Kelvar Systems</title>
<link href="https://fonts.googleapis.com/css2?family=Open+Sans:wght@400;600;700&display=swap" rel="stylesheet">
<style>
:root{
  --blue:#0a67b4;
  --green:#0aa54b;
  --ink:#222;
  --grey:#555;
  --line:#bdbdbd;
  --dark:#3a3a3a;
  --panel:#474747;
  --navy:#06111f;
}
*{box-sizing:border-box;margin:0;padding:0}
html,body{width:953px;height:1200px;overflow:hidden}
body{position:relative;background:#fff;font-family:Arial,Helvetica,sans-serif;color:var(--ink);font-size:9px}
.abs{position:absolute}
.head{font-family:"Open Sans",sans-serif}
/* header */
.topbar{left:0;top:0;width:953px;height:93px;background:linear-gradient(#fff,#f1f1f1);border-top:2px solid var(--blue);border-bottom:1px solid #d5d5d5}
.brand{left:140px;top:17px;width:120px;height:60px;border:3px solid var(--green);border-radius:4px;display:flex;align-items:center;justify-content:center;gap:5px;font-family:"Open Sans",sans-serif;font-weight:700;font-size:13px;color:var(--green)}
.brand i{width:10px;height:10px;background:var(--green);border-radius:50%}
.search{left:520px;top:26px;width:147px;height:22px;border:1px solid #ccc;background:#fff;font-style:italic;color:#777;padding:5px 6px;font-size:9px}
.call{left:688px;top:22px;display:flex;gap:6px;align-items:center}
.call small{display:block;font-size:9px;color:#333}
.call b{font-size:15px;font-weight:400;color:#111;font-family:"Open Sans",sans-serif}
.nav{left:320px;top:64px;display:flex;font-family:"Open Sans",sans-serif;font-size:10.5px;font-weight:600;color:#333}
.nav span{padding:0 12px;border-left:1px solid #bbb;line-height:13px}
.nav span:first-child{border:none;color:var(--green)}
/* slider */
.hero{left:0;top:94px;width:914px;height:331px;background:var(--navy)}
.hero-photo{left:130px;top:94px;width:687px;height:296px;background:radial-gradient(ellipse at 55% 45%,#6fa6d8 0%,#2c5d8c 45%,#0b1d33 100%)}
.arrow{width:30px;height:30px;border-radius:50%;background:#1b1b1b;border:2px solid #444;display:flex;align-items:center;justify-content:center}
.band{left:0;top:390px;width:953px;height:36px;background:linear-gradient(90deg,#0a5ca8,#0c78c8);color:#fff;font-family:"Open Sans",sans-serif;font-size:18px;text-align:center;line-height:36px}
/* section heads */
.h2{font-family:"Open Sans",sans-serif;font-weight:600;font-size:16px;color:var(--blue);border-bottom:1px dashed var(--line);padding-bottom:3px}
.svc{width:120px;text-align:center}
.svc h3{font-family:"Open Sans",sans-serif;font-size:10.5px;font-weight:600;color:#333;margin-bottom:9px}
.svc .ring{width:96px;height:96px;margin:0 auto;border-radius:50%;background:radial-gradient(#fff 55%,#e6e6e6);border:1px solid #ddd;display:flex;align-items:center;justify-content:center;box-shadow:0 6px 6px -4px #bbb}
.svc.on h3{color:var(--green)}
.svc.on .ring{border:4px solid var(--green);background:#fff}
.svc p{margin-top:14px;font-size:9px;line-height:14px;color:#333}
.para{font-size:8.4px;line-height:12.7px;color:#333;text-align:justify}
.more{color:var(--green);font-weight:700;font-size:8.5px}
.quote{font-size:8.8px;line-height:14.7px;color:#555}
.who{font-weight:700;font-size:8.3px;text-align:right;color:#222}
.field{width:204px;height:22px;border:1px solid #c8c8c8;border-radius:2px;font-style:italic;color:#666;padding:5px 8px;font-size:8.5px;box-shadow:inset 0 1px 2px #eee}
.submit{background:var(--green);color:#fff;font-weight:700;font-size:10px;padding:3px 7px;border-radius:2px}
.client{font-family:"Open Sans",sans-serif;font-weight:700;font-size:17px;color:#555;width:130px;text-align:center}
/* footer */
.foot{left:0;top:1085px;width:953px;height:115px;background:var(--dark);border-top:2px solid #222}
.box{background:var(--panel);border:1px solid #555;color:#fff;padding:7px 8px}
.box h4{font-family:"Open Sans",sans-serif;font-weight:600;font-size:10.5px;margin-bottom:7px}
.links{left:140px;top:1177px;color:#fff;font-size:8.5px}
.links span:first-child{color:var(--green)}
.sq{width:18px;height:18px;border-radius:3px;display:inline-block;margin-right:8px}
</style>
</head>
<body>
<div class="abs topbar"></div>
<div class="abs brand"><i></i>Kelvar Systems</div>
<div class="abs search">search
  <svg class="abs" style="right:6px;top:5px" width="11" height="11" viewBox="0 0 11 11"><circle cx="4.5" cy="4.5" r="3.5" fill="none" stroke="#888" stroke-width="1.4"/><path d="M7 7l3 3" stroke="#888" stroke-width="1.6"/></svg>
</div>
<div class="abs call">
  <svg width="24" height="24" viewBox="0 0 24 24"><circle cx="12" cy="12" r="10.5" fill="none" stroke="var(--green)" stroke-width="1.6"/><path d="M9 6c-2 1-2 4 0 7s5 5 7 4l-1.5-2.5-2 .8-3-3.5 1-1.7z" fill="var(--green)"/></svg>
  <div><small>Call Us Today</small><b>088-410-5270</b></div>
</div>
<div class="abs nav"><span>HOME</span><span>ABOUT US</span><span>SERVICES</span><span>SUPPORT</span><span>TESTIMONIALS</span><span>CLIENTS</span><span>CONTACT US</span></div>

<div class="abs hero"></div>
<div class="abs hero-photo" role="img" aria-label="Finger touching a glowing app tile among blurred blue squares"></div>
<div class="abs arrow" style="left:142px;top:233px"><svg width="10" height="12"><path d="M7 1L2 6l5 5" fill="none" stroke="#fff" stroke-width="1.6"/></svg></div>
<div class="abs arrow" style="left:780px;top:233px"><svg width="10" height="12"><path d="M3 1l5 5-5 5" fill="none" stroke="#fff" stroke-width="1.6"/></svg></div>
<div class="abs band">WE HAVE SPECIALISED ENGINEERS, TRAINED TO DO SPECIALISED WORK</div>

<div class="abs h2" style="left:147px;top:456px;width:670px">Our Services</div>
<svg class="abs" style="left:788px;top:464px" width="26" height="10"><path d="M6 1L2 5l4 4" fill="none" stroke="#777" stroke-width="1.2"/><path d="M19 1l4 4-4 4" fill="none" stroke="var(--green)" stroke-width="1.2"/></svg>

<div class="abs svc on" style="left:138px;top:502px"><h3>On-site Service</h3><div class="ring">
  <svg width="50" height="50" viewBox="0 0 50 50"><path d="M10 40L32 18M14 12l24 26" stroke="var(--green)" stroke-width="6" stroke-linecap="round"/><rect x="30" y="8" width="14" height="8" fill="var(--green)" transform="rotate(45 37 12)"/></svg></div>
  <p>Lorem ipsum dolor sit amet ummy nibh eui smod</p></div>
<div class="abs svc" style="left:276px;top:502px"><h3>Remote Desktop</h3><div class="ring">
  <svg width="52" height="44" viewBox="0 0 52 44"><rect x="3" y="4" width="30" height="22" rx="2" fill="none" stroke="#444" stroke-width="3"/><path d="M12 32h12" stroke="#444" stroke-width="3"/><circle cx="36" cy="28" r="11" fill="#eee" stroke="#444" stroke-width="3"/></svg></div>
  <p>Lorem ipsum dolor sit amet ummy nibh eui smod</p></div>
<div class="abs svc" style="left:415px;top:502px"><h3>Medical IT Service</h3><div class="ring">
  <svg width="50" height="46" viewBox="0 0 50 46"><path d="M8 6v12a10 10 0 0020 0V6M18 28v8a6 6 0 0012 0v-4" fill="none" stroke="#444" stroke-width="3"/><circle cx="38" cy="14" r="6" fill="none" stroke="#444" stroke-width="3"/></svg></div>
  <p>Lorem ipsum dolor sit amet ummy nibh eui smod</p></div>
<div class="abs svc" style="left:553px;top:502px"><h3>Pharmacy IT</h3><div class="ring">
  <svg width="50" height="46" viewBox="0 0 50 46"><rect x="4" y="4" width="34" height="26" fill="none" stroke="#444" stroke-width="3"/><path d="M9 24l7-8 6 5 8-10" fill="none" stroke="#444" stroke-width="2"/><circle cx="36" cy="32" r="7" fill="#eee" stroke="#444" stroke-width="3"/><path d="M41 37l5 5" stroke="#444" stroke-width="3"/></svg></div>
  <p>Lorem ipsum dolor sit amet ummy nibh eui smod</p></div>
<div class="abs svc" style="left:692px;top:502px"><h3>Website Design</h3><div class="ring">
  <svg width="50" height="46" viewBox="0 0 50 46"><rect x="4" y="6" width="40" height="26" fill="none" stroke="#444" stroke-width="3"/><path d="M18 38h14M25 32v6M18 26l14-14" stroke="#444" stroke-width="3"/></svg></div>
  <p>Lorem ipsum dolor sit amet ummy nibh eui smod</p></div>

<div class="abs" style="left:140px;top:695px;width:677px;height:1px;background:linear-gradient(90deg,transparent,#e2e2e2,transparent)"></div>

<div class="abs h2" style="left:141px;top:726px;width:204px">About Kelvar Systems</div>
<div class="abs" style="left:141px;top:760px;width:202px;height:92px;background:linear-gradient(135deg,#cdd3da,#6d7a88 55%,#2f3a47)" role="img" aria-label="Business team in a meeting"></div>
<p class="abs para" style="left:141px;top:858px;width:200px">Kelvar Systems is an Adelaide based company with a single objective - to excel in the support and service of all computer and IT needs. We provide a high level of consulting services using the most experienced engineers at a reasonable and fair price. We believe in using a Business Value approach to every</p>
<span class="abs more" style="left:288px;top:939px">Read More »</span>

<div class="abs h2" style="left:374px;top:726px;width:204px">Client Testimonials</div>
<p class="abs quote" style="left:374px;top:763px;width:208px"><b style="font-size:13px;color:#333">“</b> Nonummy nibh uismod tincidunt ut laoreet dolore magna aliquam erat volutpat. Ut wisi enim ad minim nonummy nibh euismod tincidunt <b style="font-size:13px;color:#333">”</b></p>
<p class="abs who" style="left:374px;top:808px;width:204px">Marcus Ellery-DTS</p>
<p class="abs quote" style="left:374px;top:824px;width:208px"><b style="font-size:13px;color:#333">“</b> I have always found the team extremely helpful with their advice over the phone. They also have the ability to access our computers remotely, and can rectify most problems quite swiftly. I have no hesitation in recommending Kelvar Systems for all of your IT needs.<b style="font-size:13px;color:#333">”</b></p>
<p class="abs who" style="left:374px;top:910px;width:206px">Aaron Whitfield B.Pharm<br>Harbourline Chemists, Angle Vale</p>
<span class="abs more" style="left:529px;top:939px">Read More »</span>

<div class="abs h2" style="left:608px;top:726px;width:204px">Quick Contact</div>
<div class="abs field" style="left:609px;top:760px">Name</div>
<div class="abs field" style="left:609px;top:792px">Email</div>
<div class="abs field" style="left:609px;top:824px">Phone</div>
<div class="abs field" style="left:609px;top:857px;height:60px">Message</div>
<div class="abs submit" style="left:611px;top:928px">Submit</div>

<div class="abs h2" style="left:140px;top:973px;width:678px">Our Clients</div>
<svg class="abs" style="left:780px;top:981px" width="26" height="10"><path d="M6 1L2 5l4 4" fill="none" stroke="#777" stroke-width="1.2"/><path d="M19 1l4 4-4 4" fill="none" stroke="var(--green)" stroke-width="1.2"/></svg>
<div class="abs client" style="left:132px;top:1029px">Northwind</div>
<div class="abs client" style="left:275px;top:1029px">Cloudarc</div>
<div class="abs client" style="left:398px;top:1029px">Veltrix</div>
<div class="abs client" style="left:492px;top:1029px">Strata</div>
<div class="abs client" style="left:578px;top:1029px">Helio</div>
<div class="abs client" style="left:689px;top:1029px">Quorum</div>

<div class="abs foot"></div>
<div class="abs box" style="left:139px;top:1099px;width:185px;height:58px"><h4>Subscribe to Newsletter</h4>
  <div style="display:flex;gap:6px"><div style="width:135px;height:20px;background:#5e5e5e;font-style:italic;font-size:8.5px;padding:5px 8px">Email here</div><div style="width:22px;height:20px;background:#5e5e5e;display:flex;align-items:center;justify-content:center"><svg width="8" height="10"><path d="M2 1l4 4-4 4" fill="none" stroke="#fff" stroke-width="2"/></svg></div></div></div>
<div class="abs box" style="left:363px;top:1099px;width:163px;height:58px"><h4>Contact Us</h4>
  <p style="font-size:8.5px;line-height:14px">☏ 088-410-5270<br>✉ support@kelvarsystems.com.au</p></div>
<div class="abs box" style="left:565px;top:1099px;width:88px;height:58px"><h4>Follow Us</h4>
  <span class="sq" style="background:#3b5b9a"></span><span class="sq" style="background:#39a5d8"></span><span class="sq" style="background:#e8731f;margin:0"></span></div>
<div class="abs brand" style="left:693px;top:1097px;background:#fff;height:60px">
  <i></i>Kelvar Systems</div>
<div class="abs links"><span>Home</span> | About Us | Services | Support | Testimonials | Clients | Contact Us | Terms Conditions</div>
<div class="abs" style="left:611px;top:1177px;color:#fff;font-size:8.5px">Copyright © 2014 kelvarsystems. All Rights Reserved</div>
</body>
</html>
```